Visitenkarten-Design für Rohrreinigungsfirma
Zielgruppe
Wir sind eine Kanal.-Rohrreinigungsfirma und suchen ein hochwertiges Design, unsere Zielgruppe sind Firmenkunden,Hausverwaltungen, Architekten sowie Behörden.
Aufgabenstellung
Das Design sollte Edel aussehen. Es sollten unsere Dienstleistungen mit auf der Visitenkarte stehen (gerne auch Rückseite): grabenlose Kanalsanierung, TV-Kamerainspektion,Dichtheitsprüfung DIN EN 1610, Fräsarbeiten mit Roboter, Fräsarbeiten mit Wasserhöchstdruck 2.500 Bar,Verstopfungsbeseitigung. (Vorderseite sollte enthalten:

```html
<!DOCTYPE html>
<html lang="de">
<head>
<meta charset="utf-8">
<title>Visitenkarte K.O.R.A Kanal- &amp; Rohrreinigung</title>
<link href="https://fonts.googleapis.com/css2?family=Roboto:wght@300;400;500;700&display=swap" rel="stylesheet">
<style>
  :root {
    --bg: #e4e4e4;
    --card: #ffffff;
    --navy: #0f4a6e;
    --brand-blue: #3f6c96;
    --charcoal: #3a3d42;
    --alert-red: #c8202a;
    --grey-text: #666a6e;
  }
  * { margin: 0; padding: 0; box-sizing: border-box; }
  html, body {
    width: 1150px; height: 1200px; overflow: hidden;
    background: var(--bg);
    font-family: "Roboto", Arial, sans-serif;
  }
  .card {
    position: absolute;
    left: 304px;
    width: 548px; height: 355px;
    background: var(--card);
  }
  .card-front { top: 215px; }
  .card-back { top: 652px; }

  .brand-block {
    position: absolute; left: 121px; top: 62px;
    width: 300px;
  }
  .brand-name {
    display: flex; align-items: center; gap: 10px;
    font-weight: 700; font-size: 50px; line-height: 1;
    color: var(--brand-blue); letter-spacing: -1px;
  }
  .brand-dot {
    width: 30px; height: 30px; border-radius: 50%;
    background: var(--brand-blue);
  }
  .brand-trade {
    margin-top: 8px;
    font-weight: 700; font-size: 20px; color: var(--charcoal);
    letter-spacing: 0.3px;
  }
  .brand-emergency {
    margin-top: 5px; margin-left: 55px;
    font-weight: 400; font-size: 13.5px; color: var(--alert-red);
  }

  .company-details {
    position: absolute; left: 180px; top: 204px;
    list-style: none;
    font-weight: 500; font-size: 20px; line-height: 24.5px;
    color: var(--navy);
  }

  .service-list {
    position: absolute; left: 51px; top: 50px;
    list-style: none;
    font-weight: 500; font-size: 20px; line-height: 24.7px;
    color: var(--navy);
  }
  .service-list li::before { content: "·"; }

  .contact-details {
    position: absolute; right: 53px; top: 234px;
    list-style: none; text-align: right;
    font-weight: 300; font-size: 20px; line-height: 24.7px;
    color: var(--grey-text);
  }
</style>
</head>
<body>
  <section class="card card-front">
    <div class="brand-block">
      <div class="brand-name"><span>KORA</span><span class="brand-dot"></span></div>
      <div class="brand-trade">KANAL- &amp; ROHRREINIGUNG</div>
      <div class="brand-emergency">24 STUNDEN NOTDIENST</div>
    </div>
    <ul class="company-details">
      <li>K.O.R.A Kanal.-Rohrreinigung</li>
      <li>Geschäftsführer: Lukas Brenner</li>
      <li>Talweg 14</li>
      <li>71234 Neustadt/Bergheim</li>
    </ul>
  </section>

  <section class="card card-back">
    <ul class="service-list">
      <li>grabenlose Kanalsanierung</li>
      <li>TV-Kamerainspektion</li>
      <li>Dichtheitsprüfung DIN EN 1610</li>
      <li>Fräsarbeiten mit Roboter</li>
      <li>Fräsarbeiten mit Wasserhöchstdruck 2.500 Bar</li>
      <li>Verstopfungsbeseitigung</li>
    </ul>
    <ul class="contact-details">
      <li>Tel.: 07000/123 45 67</li>
      <li>Mobil: 0151/000 111 22</li>
      <li>Email: info@rohrreinigung-kora.de</li>
    </ul>
  </section>
</body>
</html>
```